Project Name Card Design, Verdano Cargo

Company Profile
Verdano Cargo Sdn Bhd is a well-established and experienced freight forwarder in Kuala Lumpur, Malaysia. We specialize in air and sea forwarding, Custom Brokerage and regulatory compliance services, inland transportation, overseas freighting and warehousing and distribution management. With our dedicated qualified and experienced professionals, we are fully committed to serving our clients.

Our Mission
Based on the motto “Quick, Reliable and Polite”, Verdano Cargo is dedicated to upholding the following three points corporate philosophy:1. Adhering to the principle that “the customer always comes first”.2. Contributing to the development of the local community.3. Making it our duty to be responsible and sincere.

Our Edge
• One-Stop Logistics Solutions
• Extensive Network Throughout Malaysia
• Highly Qualified and Experienced Pool of Professionals
• Comprehensive IT Solutions
• Innovative and Customer-focused Solutions
• Flexible and Consistent in Managing Exceptions
• Total Supply Chain Visibility

Target Market : We sell the logistics services to all the industry in Malaysia. (One Stop Logistics Solutions)

Business Card Detail : I would like to see the logo on the front with the general info.

Must Haves :
1) Name, Title, Office, Cell, Fax, Email, Address, Website
2) Must have complete company name show as : Verdano Cargo Sdn Bhd
3) Must have company registration no, show as : 8057146-P

Nice to Haves : Modern Design Business Card

Target Market(s)

We sell the logistics services to all the industry in Malaysia. (One Stop Logistics Solutions)

Contact Information for Business Card

I would like to see the logo on the front with the general info.

Colors

Designer to choose colors to be used in the design.

Requirements
Must have
• 1) Name, Title, Office, Cell, Fax, Email, Address, Website
• 2) Must have complete company name show as : Verdano Cargo Sdn Bhd
• 3) Must have company registration no, show as : 8057146-P
Nice to have
• Modern Design Business Card
Should not have
• Nil

```html
<!DOCTYPE html>
<html lang="en">
<head>
<meta charset="utf-8">
<title>Verdano Cargo – Name Card</title>
<link href="https://fonts.googleapis.com/css2?family=Open+Sans:wght@400;600;700&display=swap" rel="stylesheet">
<style>
  :root {
    --navy: #0f5192;
    --sky: #2ba3e0;
    --paper: #ffffff;
    --ink-grey: #5a5a5a;
    --stage: #2b2b2b;
  }
  html, body {
    margin: 0;
    padding: 0;
    width: 1200px;
    height: 892px;
    overflow: hidden;
    background: var(--stage);
    font-family: "Open Sans", Arial, sans-serif;
  }
  .stage {
    position: relative;
    width: 1200px;
    height: 892px;
  }
  .card {
    position: absolute;
    width: 560px;
    height: 320px;
    background: var(--paper);
    overflow: hidden;
    box-shadow: 0 8px 24px rgba(0,0,0,0.45);
  }
  /* Front */
  .card-front { left: 90px; top: 80px; }
  .front-brand {
    position: absolute;
    left: 0; right: 0; top: 112px;
    display: flex;
    align-items: center;
    justify-content: center;
    gap: 16px;
  }
  .brand-dot {
    width: 52px; height: 52px;
    border-radius: 50%;
    background: var(--navy);
  }
  .brand-divider {
    width: 2px; height: 62px;
    background: var(--navy);
  }
  .brand-name {
    color: var(--navy);
    font-weight: 700;
    font-size: 38px;
    letter-spacing: 1px;
    text-transform: uppercase;
    line-height: 1;
  }
  .front-tagline {
    position: absolute;
    left: 0; right: 0; top: 232px;
    text-align: center;
    color: var(--ink-grey);
    font-size: 15px;
  }
  /* Back */
  .card-back { left: 550px; top: 490px; }
  .back-panel { position: absolute; inset: 0; }
  .reg-no {
    position: absolute;
    left: 24px; top: 26px;
    color: var(--ink-grey);
    font-size: 12px;
  }
  .back-brand {
    position: absolute;
    left: 24px; top: 80px;
    width: 190px;
    display: flex;
    flex-direction: column;
    align-items: center;
    gap: 14px;
  }
  .back-ring {
    width: 150px; height: 150px;
    border-radius: 50%;
    border: 10px solid var(--navy);
    box-sizing: border-box;
  }
  .back-brand-name {
    color: var(--navy);
    font-weight: 700;
    font-size: 20px;
    text-transform: uppercase;
    letter-spacing: 1px;
    white-space: nowrap;
  }
  .contact {
    position: absolute;
    right: 20px; top: 22px;
    width: 250px;
    text-align: right;
    color: var(--paper);
    font-size: 12px;
    line-height: 1.4;
    white-space: nowrap;
  }
  .person-name {
    font-weight: 700;
    font-size: 19px;
    text-transform: uppercase;
    line-height: 1.1;
  }
  .person-title { font-size: 13px; margin-bottom: 16px; }
  .address { margin-bottom: 2px; }
  .line { display: flex; justify-content: flex-end; align-items: center; gap: 8px; }
  .line svg { width: 12px; height: 12px; flex: none; }
  .web-line { margin-top: 4px; }
</style>
</head>
<body>
<main class="stage">

  <section class="card card-front" aria-label="Card front">
    <div class="front-brand">
      <span class="brand-dot"></span>
      <span class="brand-divider"></span>
      <span class="brand-name">Verdano Cargo</span>
    </div>
    <p class="front-tagline">One Stop Logistics Specialist</p>
  </section>

  <section class="card card-back" aria-label="Card back">
    <svg class="back-panel" viewBox="0 0 560 320" preserveAspectRatio="none">
      <polygon points="228,0 560,0 560,320 282,320 282,140 228,140" fill="var(--navy)"/>
    </svg>
    <div class="reg-no">Reg No: 8057146-P</div>
    <div class="back-brand">
      <span class="back-ring"></span>
      <span class="back-brand-name">Verdano Cargo</span>
    </div>
    <div class="contact">
      <div class="person-name">Daniel Tan</div>
      <div class="person-title">Managing Director</div>
      <div class="address">
        Verdano Cargo Sdn Bhd<br>
        No.8B, 2nd Floor,<br>
        Jalan Seri Mutiara 3/KS2,<br>
        Taman Mutiara Indah, 41050 Klang,<br>
        Selangor Darul Ehsan, Malaysia.
      </div>
      <div class="line">(+603) 3371 5820 / 5821
        <svg viewBox="0 0 12 12"><path d="M2 1h3l1 3-2 1a7 7 0 0 0 3 3l1-2 3 1v3c-6 0-9-3-9-9z" fill="currentColor"/></svg></div>
      <div class="line">(+6012) 486 2097
        <svg viewBox="0 0 12 12"><rect x="3" y="0.5" width="6" height="11" rx="1" fill="none" stroke="currentColor"/><circle cx="6" cy="9.5" r="0.8" fill="currentColor"/></svg></div>
      <div class="line">(+603) 3371 5822
        <svg viewBox="0 0 12 12"><rect x="1" y="5" width="10" height="5" fill="currentColor"/><rect x="3" y="1" width="6" height="4" fill="none" stroke="currentColor"/></svg></div>
      <div class="line">daniel.tan@verdanocargo.com.my
        <svg viewBox="0 0 12 12"><rect x="1" y="2.5" width="10" height="7" fill="none" stroke="currentColor"/><path d="M1 2.5l5 4 5-4" fill="none" stroke="currentColor"/></svg></div>
      <div class="line web-line">www.verdanocargo.com.my
        <svg viewBox="0 0 12 12"><circle cx="6" cy="6" r="5" fill="none" stroke="currentColor"/><path d="M1 6h10M6 1c-2.5 3-2.5 7 0 10M6 1c2.5 3 2.5 7 0 10" fill="none" stroke="currentColor" stroke-width="0.8"/></svg></div>
    </div>
  </section>

</main>
</body>
</html>
```